Savour and Thrive Wellbeing is being Launched and needs a business card and stationery package

I need a stationery package including business card (primary focus) , letterhead, digital letterhead, envelopes, with compliments slip, A 5 note sheet for the rebranding of my business and launch of my new website. I have a logo, like beige, brown earthy tones with a hint of red. I would also like the option of my letterhead also being printed on recycled paper in another format as well as the traditional letterhead. I do also send my letters to GPs and specialists digitally as well. I like to stand out from the usual stereotype of fruits and vegetables on business cards as I find that quite tacky and stereotypical. I want the business card to capture the essence of my logo as natural, nutrition, enjoyment, nurturing and freedom with food. I have attached the logo, and additional brief sheet on my ideas. Happy to have any background that is complementary to my theme, and what you believe would be catching. Definitely DONT'T like pink, try to pick up the darker colour in the logo please. and think too much black is a little overpowering.

Target Market(s)

clients who are interested in improving their health and wellness. Client 80% females; 20% males

Industry/Entity Type

Health And Wellness

Contact Information for Business Card

I am open to having different backgrounds as well that would complement the logo. Probably less emphasis on the heart out of the logo - just happy to keep that in the logo only please
I am also wanting two business cards - one for the appointments, one for general distribution and media distribution (both need to look consistent though) - but does give opportunity for one of the business cards to be less wordy and more striking. And the front of the business card can certainly stand out with the entire savour and thrive logo and my name and grab the attention of the receiver.
1st business card
on front:
Lorena Whitcombe
Savour and Thrive Wellbeing & logo
Nutritionist and Dietitian
Tarvel Medical Centre
647 Brindle Hill Rd, Quorrel Q 4987
Phone: (07) 3017 2968 Fax: (07) 3156 7209
Mobile: 0400 261 937
www.savourandthrivewellbeing.example.au
lorena@savourandthrivewellbeing.example.au
on back:
next appointment

……………………….. at ……………………… (possibly 4 times)
If you are unable to keep your appointment, please contact us as soon as possible (small font)
2nd business card (needs to be very eye catching and stand out)
on front: Savour and Thrive Wellbeing logo and my name
on back:
Lorena Whitcombe
address
phones, fax, website, email address

Font styles to use
Other font styles liked:
• please refer to logo

Requirements
Must have
• refreshing and simple; new and vibrant - I am rebranding my business after 20 years
• to get a feel of what is the theme - go to my new website (not completed as yet - but you will get a preliminary view) - don't do as google search as blocked - but can put into website header and it will be shown
• www.savourandthrivewellbeing.example.au - but please ignore the colouring of the 4 blocks under the slider on the home page - I am not wanting these colourings - they are getting updated.
Nice to have
• earthy tones, beige, hint of red, fonts to match logo if possible, organic, modern
• get inspiration from my logo please, open to having other backgrounds that complement
Should not have
• no food shots or stereotypical weight/ scales images
• no green, yellow or orange

```html
<!DOCTYPE html>
<html lang="en">
<head>
<meta charset="utf-8">
<title>Savour and Thrive Wellbeing – Business Cards</title>
<link href="https://fonts.googleapis.com/css2?family=Roboto:wght@400;500&display=swap" rel="stylesheet">
<style>
  :root {
    --backdrop: #e3e3e5;
    --paper: #f4f3f0;
    --ink: #2a2326;
    --ink-soft: #4a4245;
    --accent: #b0424f;
    --motif-grey: #e4e2de;
    --motif-blush: #efd3d2;
    --dots: #6a6265;
  }
  * { box-sizing: border-box; margin: 0; padding: 0; }
  html, body {
    width: 1200px; height: 800px; overflow: hidden;
    background: var(--backdrop);
    font-family: "Roboto", Arial, sans-serif;
    color: var(--ink);
  }
  .canvas { position: relative; width: 1200px; height: 800px; }

  .card {
    position: absolute;
    background: var(--paper);
    box-shadow: 0 10px 28px rgba(0,0,0,0.12), 0 2px 4px rgba(0,0,0,0.08);
    overflow: hidden;
  }

  /* Front card */
  .card-front { left: 70px; top: 230px; width: 580px; height: 350px; }
  .card-front .motif {
    position: absolute; left: -40px; top: -30px; width: 330px; height: 300px;
    border-radius: 0 0 60% 40%;
    background: radial-gradient(circle at 45% 40%, var(--motif-grey), rgba(228,226,222,0) 70%);
  }
  .brand {
    display: flex; align-items: center; gap: 12px;
  }
  .brand-dot {
    width: 26px; height: 26px; border-radius: 50%; background: var(--accent); flex: none;
  }
  .brand-name {
    font-weight: 400; color: var(--ink); letter-spacing: 0.5px; line-height: 1.1;
  }
  .card-front .brand { position: absolute; left: 250px; top: 50px; }
  .card-front .brand-name { font-size: 27px; width: 260px; }

  .holder { position: absolute; left: 250px; top: 150px; }
  .holder-name { font-size: 21px; font-weight: 500; color: var(--ink); }
  .holder-role { font-size: 14px; color: var(--accent); margin-top: 3px; }

  .contact {
    position: absolute; left: 40px; top: 215px; width: 510px;
    font-size: 13px; line-height: 1.55; color: var(--ink-soft);
  }
  .contact-split { display: flex; gap: 12px; }
  .contact-split .col-right { border-left: 1px solid var(--ink-soft); padding-left: 12px; }

  /* Back card */
  .card-back { left: 760px; top: 110px; width: 350px; height: 580px; }
  .card-back .motif {
    position: absolute; left: 40px; top: 300px; width: 330px; height: 300px;
    border-radius: 50% 50% 0 0;
    background: radial-gradient(circle at 50% 55%, var(--motif-blush), rgba(239,211,210,0) 72%);
  }
  .card-back .brand { position: absolute; left: 40px; top: 60px; }
  .card-back .brand-name { font-size: 24px; width: 240px; }

  .appointments { position: absolute; left: 40px; top: 190px; width: 270px; }
  .appointments-title { font-size: 15px; color: var(--ink); margin-bottom: 26px; }
  .slot {
    display: flex; align-items: flex-end; gap: 8px; height: 54px;
    font-size: 13px; color: var(--ink-soft);
  }
  .slot .line { flex: 1; border-bottom: 2px dotted var(--dots); height: 1px; margin-bottom: 4px; }
  .slot .line.short { flex: 0.6; }
</style>
</head>
<body>
<main class="canvas">

  <section class="card card-front" aria-label="Business card front">
    <div class="motif" role="img" aria-label="Faint large leaf motif in light grey"></div>

    <div class="brand">
      <span class="brand-dot"></span>
      <span class="brand-name">Savour and Thrive Wellbeing</span>
    </div>

    <div class="holder">
      <p class="holder-name">Lorena Whitcombe</p>
      <p class="holder-role">Nutritionist and Dietitian</p>
    </div>

    <div class="contact">
      <p>P: (07) 3017 2968 &nbsp;|&nbsp; F: (07) 3156 7209</p>
      <div class="contact-split">
        <p class="col-left">M: 0400 261 937</p>
        <p class="col-right">Tarvel Medical Centre<br>647 Brindle Hill Rd, Quorrel Q 4987</p>
      </div>
      <p>www.savourandthrivewellbeing.example.au</p>
      <p>lorena@savourandthrivewellbeing.example.au</p>
    </div>
  </section>

  <section class="card card-back" aria-label="Business card back, appointment card">
    <div class="motif" role="img" aria-label="Faint large leaf motif in soft blush"></div>

    <div class="brand">
      <span class="brand-dot"></span>
      <span class="brand-name">Savour and Thrive Wellbeing</span>
    </div>

    <div class="appointments">
      <p class="appointments-title">Next Appointment</p>
      <div class="slot"><span class="line"></span><span>at</span><span class="line short"></span></div>
      <div class="slot"><span class="line"></span><span>at</span><span class="line short"></span></div>
      <div class="slot"><span class="line"></span><span>at</span><span class="line short"></span></div>
      <div class="slot"><span class="line"></span><span>at</span><span class="line short"></span></div>
    </div>
  </section>

</main>
</body>
</html>
```